Harvest Gathering event flyer

I would like a church event flyer designed. The event is called "HARVEST GATHERING 2018". I am looking for a professional, yet catchy design that uses our brand colors and logo creatively while communicating key information of the event effectively.

1. The logo is attached in two color formats. The designer has the choice to use them as he/she want.

2. The location of the event is: Lindqvist Community Center, 482 Tamsworth Street, Portland, ME 04102
3. Time and date of event. The designer can organize and format the date and time as he/she pleases.
December 28th, 29th @ 7:00PM
December 30th @ 10:00AM
4. The topic of the event is "Tongues of fire". The designer is free to use this phrase as he/she pleases to create a good composition.
5. Speaker: Prophet Marcus Obuya
6. Contact information: contact@cedarbrookfellowship.org - Telephone number: 207 555 0148

7. I would also like the following three words on the flyer. These words describe the focus of the event: FIRE, REVIVAL, PROPHETIC

```html
<!DOCTYPE html>
<html lang="en">
<head>
<meta charset="utf-8">
<title>Harvest Gathering 2018 — Event Flyer</title>
<link href="https://fonts.googleapis.com/css2?family=Oswald:wght@400;600;700&family=Montserrat:wght@500;600;700&display=swap" rel="stylesheet">
<style>
  :root{
    --navy:#0d3564;
    --navy-deep:#0a2b52;
    --orange:#f7941d;
    --white:#ffffff;
    --cream:#f3efe6;
    --ink:#1c1c1c;
    --page:#e9e9ea;
  }
  *{box-sizing:border-box;margin:0;padding:0}
  html,body{width:1200px;height:1200px;overflow:hidden;background:var(--page)}
  .flyer{
    position:absolute;left:200px;top:35px;width:800px;height:1130px;
    background:var(--navy);overflow:hidden;
    box-shadow:0 10px 30px rgba(0,0,0,.18);
    font-family:"Montserrat",sans-serif;color:var(--white);
  }
  .photo-frame{position:absolute;left:0;top:0;width:800px;height:560px}
  .brand{
    position:absolute;left:52px;top:250px;display:flex;align-items:center;gap:12px;
    font-family:"Montserrat",sans-serif;font-weight:600;font-size:36px;letter-spacing:4px;color:var(--white);
  }
  .brand-dot{width:22px;height:22px;border-radius:50%;background:var(--orange)}
  .event-title{
    position:absolute;left:52px;top:318px;
    font-family:"Oswald",sans-serif;font-weight:700;line-height:.98;font-size:58px;text-transform:uppercase;
  }
  .event-title .accent{color:var(--orange)}
  .topic{
    position:absolute;left:52px;top:520px;
    font-family:"Oswald",sans-serif;font-weight:400;font-size:34px;color:var(--orange);text-transform:uppercase;letter-spacing:.5px;
  }
  .focus-list{position:absolute;left:60px;top:575px;list-style:none}
  .focus-list li{
    display:flex;align-items:center;gap:14px;margin-bottom:8px;
    font-family:"Oswald",sans-serif;font-size:20px;letter-spacing:.5px;
  }
  .focus-list li:nth-child(2){margin-left:34px}
  .focus-list li:nth-child(3){margin-left:68px}
  .focus-icon{width:30px;height:30px;border:2px solid var(--orange);border-radius:50%;display:flex;align-items:center;justify-content:center}
  .focus-icon span{width:10px;height:10px;background:var(--orange);border-radius:50%}
  .speaker{position:absolute;left:52px;top:720px;font-size:27px;font-weight:600;line-height:1.25}
  .speaker .label{color:var(--orange);font-weight:700;letter-spacing:1px}
  .info-row{position:absolute;left:52px;display:flex;align-items:center;gap:28px}
  .info-row.dates{top:815px}
  .info-row.venue{top:940px}
  .info-icon{
    width:82px;height:82px;border-radius:50%;border:3px solid var(--orange);
    background:var(--navy-deep);display:flex;align-items:center;justify-content:center;flex:none;
    box-shadow:0 0 0 4px var(--white) inset;
  }
  .info-text{font-size:28px;font-weight:600;line-height:1.3}
  .info-text .hl{color:var(--orange)}
  .venue-name{color:var(--orange);font-size:30px;font-weight:700;text-transform:uppercase;letter-spacing:.5px}
  .venue-address{font-size:22px;font-weight:600}
  .contact-bar{
    position:absolute;left:0;bottom:0;width:100%;height:70px;background:var(--white);
    display:flex;align-items:center;justify-content:space-around;padding:0 30px;
    color:var(--ink);font-size:17px;font-weight:500;
  }
  .contact-item{display:flex;align-items:center;gap:10px}
  .contact-item:first-child{font-size:21px;font-weight:600}
</style>
</head>
<body>
<main class="flyer">
  <svg class="photo-frame" viewBox="0 0 800 560">
    <defs>
      <linearGradient id="portraitFill" x1="0" y1="0" x2="1" y2="1">
        <stop offset="0" stop-color="#f3efe6"/>
        <stop offset=".55" stop-color="#9a8f86"/>
        <stop offset="1" stop-color="#1d1d22"/>
      </linearGradient>
    </defs>
    <rect x="0" y="0" width="800" height="70" fill="#f3efe6"/>
    <circle cx="590" cy="150" r="298" fill="none" stroke="#f7941d" stroke-width="12"/>
    <circle cx="590" cy="150" r="290" fill="url(#portraitFill)" role="img" aria-label="Portrait photograph of the speaker in a dark suit and glasses"/>
  </svg>

  <div class="brand"><span class="brand-dot"></span>KAVELO</div>

  <h1 class="event-title">Harvest<br><span class="accent">Gathering</span><br>2018</h1>

  <p class="topic">Tongues of Fire</p>
  <ul class="focus-list">
    <li><span class="focus-icon"><span></span></span>FIRE</li>
    <li><span class="focus-icon"><span></span></span>REVIVAL</li>
    <li><span class="focus-icon"><span></span></span>PROPHETIC</li>
  </ul>

  <p class="speaker"><span class="label">SPEAKER:</span><br>Prophet Marcus Obuya</p>

  <div class="info-row dates">
    <div class="info-icon">
      <svg width="40" height="40" viewBox="0 0 40 40" fill="none" stroke="#fff" stroke-width="2.5">
        <rect x="5" y="8" width="30" height="27" rx="3"/>
        <line x1="5" y1="16" x2="35" y2="16"/>
        <line x1="13" y1="4" x2="13" y2="11"/>
        <line x1="27" y1="4" x2="27" y2="11"/>
      </svg>
    </div>
    <div class="info-text">
      December <span class="hl">28th, 29th</span> @ 7:00PM<br>
      December <span class="hl">30th</span> @ 10:00AM
    </div>
  </div>

  <div class="info-row venue">
    <div class="info-icon">
      <svg width="40" height="40" viewBox="0 0 40 40" fill="none" stroke="#fff" stroke-width="2.5">
        <path d="M20 36 C12 26 9 21 9 15 a11 11 0 0 1 22 0 c0 6-3 11-11 21z"/>
        <circle cx="20" cy="15" r="4"/>
      </svg>
    </div>
    <div>
      <div class="venue-name">Lindqvist Community Center</div>
      <div class="venue-address">482 Tamsworth Street, Portland, ME 04102</div>
    </div>
  </div>

  <footer class="contact-bar">
    <span class="contact-item">
      <svg width="22" height="22" viewBox="0 0 24 24" fill="#f7941d"><path d="M6.6 10.8a15 15 0 0 0 6.6 6.6l2.2-2.2c.3-.3.7-.4 1-.2 1.1.4 2.3.6 3.6.6.6 0 1 .4 1 1V20c0 .6-.4 1-1 1A17 17 0 0 1 3 4c0-.6.4-1 1-1h3.5c.6 0 1 .4 1 1 0 1.3.2 2.5.6 3.6.1.3 0 .7-.2 1z"/></svg>
      207 555 0148
    </span>
    <span class="contact-item">
      <svg width="22" height="16" viewBox="0 0 22 16" fill="#f7941d"><rect width="22" height="16" rx="2"/><path d="M1 1l10 8 10-8" stroke="#fff" stroke-width="1.6" fill="none"/></svg>
      contact@cedarbrookfellowship.org
    </span>
    <span class="contact-item">
      <svg width="20" height="20" viewBox="0 0 20 20" fill="none" stroke="#f7941d" stroke-width="1.8"><circle cx="10" cy="10" r="8.5"/><ellipse cx="10" cy="10" rx="3.8" ry="8.5"/><line x1="1.5" y1="10" x2="18.5" y2="10"/></svg>
      www.kavelo.org
    </span>
  </footer>
</main>
</body>
</html>
```